Upmarket Bathroom and Kitchen ware supplier needs a classy business card design

We are a company based in Fiji, we sell plumbing ware (Kitchen and bathroom taps, Basins,showers, toilets etc) through up market show rooms to individuals and directly through Architects and designers of resorts and holiday houses for new builds and renovations. we are wanting to upgrade our over all look and brand. we are starting with a new logo but will be rebranding the whole business. This project is for a business card design for my management and tales team I would like it to be dark, classy and interesting

Target Market(s)

Resort directors and Management, High end holiday home owners

Contact Information for Business Card

Neil Dawson
Director
+64219473815

Colors

Designer to choose colors to be used in the design.

Requirements
Must have
• Must have an upmarket appearance I like darker charcoal shades but will be guided by the designers
• Please any catch phrases like "Crafting remarkable living rooms" this belongs tpo one of our suppliers so can not be used.
Nice to have
• Double sided, so front dedicated to logo provided and back info about the business and the person.

```html
<!DOCTYPE html>
<html lang="en">
<head>
<meta charset="utf-8">
<title>Solano Interiors – Business Card</title>
<link href="https://fonts.googleapis.com/css2?family=Josefin+Sans:wght@300&family=Arimo:wght@400&display=swap" rel="stylesheet">
<style>
  :root {
    --page-bg: #e6e6e6;
    --card-bg: #141515;
    --gold-light: #f3e3b4;
    --gold-mid: #d2b48c;
    --rose-gold: #c49a7c;
    --gold-dark: #a88468;
    --name-rose: #c7a085;
    --text-cream: #f6e7b0;
  }
  * { margin: 0; padding: 0; box-sizing: border-box; }
  html, body {
    width: 1200px; height: 1000px; overflow: hidden;
    background: var(--page-bg);
  }
  .canvas { position: relative; width: 1200px; height: 1000px; }

  .card {
    position: absolute; left: 293px; width: 615px; height: 380px;
    background: var(--card-bg);
  }
  .card--back { top: 76px; }
  .card--front { top: 545px; }

  /* back: framed contact panel */
  .contact-frame {
    position: absolute; left: 182px; top: 24px; width: 251px; height: 331px;
    border: 1.5px solid var(--rose-gold);
  }
  .side-tab {
    position: absolute; top: 132px; width: 28px; height: 117px;
    border-top: 3px solid var(--gold-mid);
    border-bottom: 3px solid var(--gold-mid);
  }
  .side-tab::after {
    content: ""; position: absolute; left: 0; right: 0; top: 6px; bottom: 6px;
    background: linear-gradient(90deg, var(--gold-dark), var(--gold-light) 50%, var(--rose-gold));
  }
  .side-tab--left { left: 0; }
  .side-tab--right { right: 0; }

  .brand {
    position: absolute; left: 0; right: 0; text-align: center;
    font-family: "Josefin Sans", sans-serif; font-weight: 300;
    color: var(--rose-gold); letter-spacing: 0.22em; white-space: nowrap;
  }
  .brand-dot {
    position: absolute; border-radius: 50%;
    border: 1.5px solid var(--rose-gold);
  }
  .contact-frame .brand-dot { left: 101px; top: 54px; width: 46px; height: 46px; }
  .contact-frame .brand { top: 142px; font-size: 16px; }

  .person {
    position: absolute; left: 0; right: 0; text-align: center;
    font-family: "Arimo", sans-serif;
  }
  .person__name { top: 218px; font-size: 22px; color: var(--text-cream); }
  .person__name .first { color: var(--name-rose); }
  .person__role { top: 250px; font-size: 15px; color: var(--text-cream); }
  .person__phone { top: 280px; font-size: 17px; color: var(--text-cream); }

  /* front: logo band */
  .rule {
    position: absolute; left: 0; right: 0; height: 3px;
    background: linear-gradient(90deg, var(--rose-gold), var(--gold-light) 55%, var(--gold-mid));
  }
  .rule--top { top: 102px; }
  .rule--bottom { top: 272px; }
  .card--front .brand-dot { left: 140px; top: 166px; width: 48px; height: 48px; }
  .card--front .brand { left: 110px; top: 179px; font-size: 24px; color: var(--gold-mid); }
</style>
</head>
<body>
<main class="canvas">
  <section class="card card--back" aria-label="Card back with contact details">
    <div class="side-tab side-tab--left"></div>
    <div class="side-tab side-tab--right"></div>
    <div class="contact-frame">
      <span class="brand-dot"></span>
      <p class="brand">SOLANO INTERIORS</p>
      <p class="person person__name"><span class="first">NEIL</span> Dawson</p>
      <p class="person person__role">Director</p>
      <p class="person person__phone">+64219473815</p>
    </div>
  </section>

  <section class="card card--front" aria-label="Card front with brand name">
    <div class="rule rule--top"></div>
    <span class="brand-dot"></span>
    <p class="brand">SOLANO INTERIORS</p>
    <div class="rule rule--bottom"></div>
  </section>
</main>
</body>
</html>
```